Coastal Bright Sweep Business Card

We are a cleaning and waste management company with the slogan "making waste to landfill a thing of the past". We would like a re-design of our current business card. On the front we want to continue to use our logo as the focus point. On the back, we want the whole thing re-done to be less busy. We want the staff member’s name, the job title, mobile number, email and website. We do not want the address on the card. We still want the green, black and blue colours used, but a new font for the information on the back. Please do not change the logo design at all. We are also thinking about using icons to replace the text ‘mobile, email, website’. The “events + commercial” banner needs to be incorporated somewhere and needs to read “events + commercial + waste”. Another important point for consideration is that we are very concerned about being environmentally sustainable and will be printing on recycled paper. All designs should be made to compliment this in regards to boldness and colouring. Please find attached our logo, our colour chart and an image of our current business card.

```html
<!DOCTYPE html>
<html lang="en">
<head>
<meta charset="utf-8">
<title>Coastal Bright Sweep – Business Card</title>
<link rel="stylesheet" href="https://fonts.googleapis.com/css2?family=Lato:wght@400;700;900&family=Roboto+Slab:wght@700&display=swap">
<style>
  :root {
    --bg: #e9e6e1;
    --card-dark: #1d1d1d;
    --card-light: #ffffff;
    --brand-blue: #27a3de;
    --brand-navy: #1f4f8f;
    --brand-green: #7dc242;
    --ink: #4a4a4a;
    --paper-white: #f4f4f4;
  }
  * { margin: 0; padding: 0; box-sizing: border-box; }
  html, body {
    width: 1200px; height: 900px; overflow: hidden;
    background: var(--bg);
    font-family: "Lato", Arial, sans-serif;
  }
  .canvas {
    width: 1200px; height: 900px;
    display: flex; flex-direction: column;
    align-items: center; justify-content: center; gap: 56px;
  }
  .card {
    width: 600px; height: 343px;
    position: relative;
    box-shadow: 0 6px 18px rgba(0,0,0,.14);
  }
  /* Front */
  .card--front {
    background: var(--card-dark);
    display: flex; flex-direction: column;
    align-items: center; justify-content: center;
  }
  .brand-name {
    font-family: "Lato", Arial, sans-serif;
    font-weight: 900;
    color: var(--brand-blue);
    line-height: 0.95;
    text-align: left;
  }
  .card--front .brand-name { font-size: 56px; display: flex; align-items: center; gap: 16px; }
  .brand-dot {
    width: 18px; height: 18px; border-radius: 50%;
    background: var(--brand-green); flex: none;
  }
  .slogan {
    position: absolute; left: 0; right: 0; bottom: 40px;
    text-align: center;
    color: var(--paper-white);
    font-size: 13px; letter-spacing: 0.08em;
    text-transform: uppercase;
  }
  /* Back */
  .card--back {
    background: var(--card-light);
    display: flex; align-items: center;
    padding: 0 44px 30px 46px;
  }
  .card--back .brand-name { font-size: 38px; width: 210px; }
  .divider {
    width: 2px; height: 150px;
    background: var(--brand-green);
    margin: 0 26px 0 18px; flex: none;
  }
  .contact { display: flex; flex-direction: column; }
  .person-name {
    font-family: "Roboto Slab", Georgia, serif;
    font-weight: 700; font-size: 19px;
    letter-spacing: 0.02em; text-transform: uppercase;
  }
  .person-name .first { color: var(--brand-blue); }
  .person-name .last { color: var(--brand-green); }
  .job-title { color: var(--ink); font-size: 14px; margin: 4px 0 16px; }
  .contact-list { list-style: none; display: flex; flex-direction: column; gap: 5px; }
  .contact-item {
    display: flex; align-items: center; gap: 9px;
    color: var(--ink); font-size: 12px;
  }
  .contact-icon { width: 12px; height: 12px; flex: none; fill: var(--brand-navy); }
  .services {
    position: absolute; left: 0; right: 0; bottom: 34px;
    text-align: center;
    font-size: 14px; letter-spacing: 0.04em;
    color: var(--brand-blue);
  }
  .services .plus { color: var(--brand-green); }
</style>
</head>
<body>
<main class="canvas">
  <section class="card card--front" aria-label="Card front">
    <div class="brand-name"><span class="brand-dot"></span>Coastal Bright<br>Sweep</div>
    <p class="slogan">Making waste to landfill a thing of the past</p>
  </section>

  <section class="card card--back" aria-label="Card back">
    <div class="brand-name">Coastal<br>Bright<br>Sweep</div>
    <span class="divider"></span>
    <div class="contact">
      <h1 class="person-name"><span class="first">Morgan</span> <span class="last">Tessler</span></h1>
      <p class="job-title">Client Manager</p>
      <ul class="contact-list">
        <li class="contact-item">
          <svg class="contact-icon" viewBox="0 0 24 24" aria-hidden="true"><path d="M6.6 10.8a15.1 15.1 0 0 0 6.6 6.6l2.2-2.2a1 1 0 0 1 1-.25 11.4 11.4 0 0 0 3.6.57 1 1 0 0 1 1 1V20a1 1 0 0 1-1 1A17 17 0 0 1 3 4a1 1 0 0 1 1-1h3.5a1 1 0 0 1 1 1c0 1.25.2 2.45.57 3.57a1 1 0 0 1-.25 1z"/></svg>
          0400 555 218
        </li>
        <li class="contact-item">
          <svg class="contact-icon" viewBox="0 0 24 24" aria-hidden="true"><path d="M2 5h20v14H2z M3.5 6.5 12 13l8.5-6.5" stroke="#fff" stroke-width="1.6"/></svg>
          mtessler@coastalbrightsweep.com.au
        </li>
        <li class="contact-item">
          <svg class="contact-icon" viewBox="0 0 24 24" aria-hidden="true"><circle cx="12" cy="12" r="10"/><path d="M2 12h20M12 2c3 3 3 17 0 20M12 2c-3 3-3 17 0 20" stroke="#fff" stroke-width="1.4" fill="none"/></svg>
          www.coastalbrightsweep.com.au
        </li>
      </ul>
    </div>
    <p class="services">EVENTS <span class="plus">+</span> COMMERCIAL <span class="plus">+</span> WASTE</p>
  </section>
</main>
</body>
</html>
```